Corvane Project Services - Flyer

Project Breif:
I need a single page A4 Capability Statement, which will be used to market our services to prospective clients, both in print and via email PDF.
It needs to look professional and should incorporate the elements I have uploaded into files, these include:
Capability Statement Text
Corvane Services Company Logo
Additional Logo’s (Tools We Use)
Glimmer Bay Pics can be cut into the page
I have included examples of capability statements as a guide to what i am looking for.
Regards
Derek
Engineering Consulting

```html
<!DOCTYPE html>
<html lang="en">
<head>
<meta charset="utf-8">
<title>Corvane Project Services – Capability Statement</title>
<link href="https://fonts.googleapis.com/css2?family=Questrial&family=Michroma&display=swap" rel="stylesheet">
<style>
  :root {
    --sky: #5cb3dd;
    --sky-light: #7cc6e8;
    --steel: #5e92c9;
    --navy: #1f3f8f;
    --ink: #2b2b2b;
    --text: #3a3a3a;
    --rule: #d9dde2;
    --paper: #ffffff;
    --page: #f4f6f8;
  }
  * { box-sizing: border-box; margin: 0; padding: 0; }
  html, body { width: 848px; height: 1200px; overflow: hidden; }
  body {
    position: relative;
    background: linear-gradient(180deg, #ffffff 0%, var(--page) 100%);
    font-family: "Questrial", sans-serif;
    color: var(--text);
  }
  .brand {
    position: absolute; left: 24px; top: 40px; width: 240px;
    text-align: center;
  }
  .brand-mark {
    width: 56px; height: 56px; border-radius: 50%;
    background: var(--steel); margin: 0 auto 14px;
  }
  .brand-name {
    font-size: 21px; letter-spacing: 1px; color: var(--ink);
    border-bottom: 1px solid var(--ink); padding-bottom: 3px;
  }
  .brand-sub {
    font-size: 13px; letter-spacing: 9px; color: var(--navy); margin-top: 3px;
  }
  .title {
    position: absolute; right: 20px; top: 96px; text-align: right;
    font-family: "Michroma", sans-serif; line-height: 40px;
  }
  .title-line1 { font-size: 33px; color: var(--sky-light); }
  .title-line2 { font-size: 33px; color: var(--steel); }
  .hero {
    position: absolute; left: 0; top: 184px; width: 848px; height: 260px;
    border-top: 6px solid #8cc4e6; border-bottom: 6px solid #8fb3db;
    background: linear-gradient(100deg, #e8edf3 0%, #f4f6f9 45%, #d9e3ec 70%, #c9d3dc 100%);
  }
  .card {
    position: absolute; background: var(--paper);
    border: 1px solid var(--rule); box-shadow: 0 1px 3px rgba(0,0,0,.08);
    padding: 8px 20px;
  }
  .card h2 {
    font-weight: 400; font-size: 19px; color: var(--sky); line-height: 22px; margin-bottom: 2px;
  }
  .card p, .card li {
    font-size: 15px; line-height: 18.8px; list-style: none;
  }
  .about { left: 16px; top: 458px; width: 411px; height: 187px; }
  .team { left: 16px; top: 654px; width: 411px; height: 118px; }
  .expertise { left: 16px; top: 784px; width: 411px; height: 321px; }
  .core-heading {
    position: absolute; left: 460px; top: 452px;
    font-size: 24px; font-weight: 400; color: var(--sky);
  }
  .planning { left: 446px; top: 482px; width: 380px; height: 163px; }
  .risk { left: 446px; top: 654px; width: 380px; height: 160px; }
  .risk h2 { margin-bottom: 6px; }
  .cost { left: 446px; top: 830px; width: 380px; height: 116px; }
  .cost h2 { margin-bottom: 8px; }
  .contact { left: 446px; top: 962px; width: 380px; height: 143px; }
  .contact h2 { margin-bottom: 16px; }
  .contact li { line-height: 21.5px; }
  .tools {
    position: absolute; left: 20px; top: 1130px; width: 808px; height: 44px;
    display: flex; justify-content: space-between; align-items: center;
  }
  .tool {
    display: flex; align-items: center; gap: 6px;
    font-size: 15px; color: var(--navy);
  }
  .tool-dot { width: 12px; height: 12px; background: var(--steel); }
</style>
</head>
<body>
  <header>
    <div class="brand">
      <div class="brand-mark"></div>
      <div class="brand-name">CORVANE PROJECT</div>
      <div class="brand-sub">SERVICES</div>
    </div>
    <h1 class="title">
      <div class="title-line1">COMPATIBILITY</div>
      <div class="title-line2">STATEMENT</div>
    </h1>
  </header>

  <div class="hero" role="img" aria-label="Photo of a printed Gantt schedule with a pen, beside colleagues reviewing documents at a desk"></div>

  <section class="card about">
    <h2>About Us:</h2>
    <p>Our goal is to make successful project delivery more achievable and repeatable.<br>
    We are continually innovating, evolving and learning, utilizing the latest industry tools and techniques to deliver real value to our clients.<br>
    We are passionate about empowering organisations to achieve their objectives, on time and on budget.</p>
  </section>

  <section class="card team">
    <h2>Our Team</h2>
    <p>We use highly experienced industry professionals who engage with our clients to deliver practical and innovative project control solutions.</p>
  </section>

  <section class="card expertise">
    <h2>Our Expertise</h2>
    <p>For over 20 years we have been helping our clients to successfully deliver capital projects within the pharmaceutical and biotechnology sectors.<br>
    During this time, we have worked closely with multinational healthcare companies and leading A&amp;E firms, on a variety of business-critical projects.<br>
    Our experience and knowledge of project control gives our client’s unparalleled visibility of Cost, Schedule and Risk through the lifecycle of their projects.<br>
    This visibility allows our clients to make timely informed decisions which increase efficiency and project performance.</p>
  </section>

  <h2 class="core-heading">Core Services:</h2>

  <section class="card planning">
    <h2>Planning and Scheduling</h2>
    <ul>
      <li>Tender Planning</li>
      <li>Interactive Planning / Pull Planning</li>
      <li>EPCMV Planning &amp; Scheduling</li>
      <li>Schedule Earned Value Management</li>
      <li>Independent Schedule Quality Assessment</li>
      <li>Schedule Risk Analysis (Monte Carlo)</li>
      <li>Training</li>
    </ul>
  </section>

  <section class="card risk">
    <h2>Management of Risk</h2>
    <ul>
      <li>Risk Management Policies &amp; Procedures</li>
      <li>Risk Management Strategy</li>
      <li>Risk Registers</li>
      <li>Risk Improvement Planning</li>
      <li>Risk Response and Communication</li>
      <li>Risk Management Training</li>
    </ul>
  </section>

  <section class="card cost">
    <h2>Cost Control:</h2>
    <ul>
      <li>Estimating &amp; Forecasting</li>
      <li>Earned Value Analysis</li>
      <li>Progress Reporting</li>
      <li>Cost Risk Analysis</li>
    </ul>
  </section>

  <section class="card contact">
    <h2>Contact:</h2>
    <ul>
      <li>info@corvaneservices.ie</li>
      <li>www.corvaneservices.ie</li>
      <li>+353 (0)870 114 562</li>
    </ul>
  </section>

  <footer class="tools">
    <span class="tool"><span class="tool-dot"></span>Keystone Planner</span>
    <span class="tool"><span class="tool-dot"></span>Tasklane</span>
    <span class="tool"><span class="tool-dot"></span>Meridian Schedule</span>
    <span class="tool"><span class="tool-dot"></span>Waypoint Pro</span>
    <span class="tool"><span class="tool-dot"></span>Tallyline</span>
    <span class="tool"><span class="tool-dot"></span>RiskForm</span>
  </footer>
</body>
</html>
```